MARLSTONE BUILDWORKS B-Card

I currently have a b-card design but will be removing the image (tree) from the logo and have text only.
I want the card to be classy and strong within the building and construction industry.
I will be using Spot UV on the cards as per the attached examples. I will also send through some sketched ideas that I have in mind.
The color blue is similar to the image (No. 6) attached images

Target Market(s)

middle to maturre aged.
Home Owners / Renovators and Builders

Industry/Entity Type

Construction

Contact Information for Business Card

MARLSTONE BUILDWORKS
Name: Gideon Pellow
Title: Project Manager
Mobile: 0472 315 084
Office: (08) 9571 2046
Address: 17C Quenby Parade, Malaga WA 6090
Email: info@marlstonehouses.example.au
PO Box: 3817 Malaga WA 6944

Colors
0592cd
33a6d7
85cae6
1b1b1b

Requirements
Must have
• 1. It must have spot UV on the front of card, maybe back of card too
• 2. I really like the blue on image 6. (or at least a really cool electric blue against the charcoal grey background)
• 3. The font must be slimline and modern. Easy to read
• 4. There must be no black used on the card... Only greys and dark charcoal greys
• 5. Use only the text from the logo "Marlstone Buildworks" Not the image of the tree. I am wanting the b-cards to be more masculine.
Nice to have
• 1. I like the design concept on image 6. but happy to see what else you can do with the Spot UV
• 2. Unless you have a really cool idea of the image of the tree (from previous logo) Spot UV somewhere in the design concept thats original and different then I am keen to see what you come up with
• 3. Try changing the color of the logo eg. full white or Blue and white
• 4. Another option is to have the Marlstone Logo on the front of card with the spot UV in the background of text which we specialise in eg, Roofing, Ceiling, Insulation, Gutter Guards, Electrical, Insurance etc and we can add or reduce items as required. Similar to image 12.
Should not have
• Do not include the image of the tree from previous logo. unless you have a really cool idea of Spot UV somewhere in the design concept thats original and different.

```html
<!DOCTYPE html>
<html lang="en">
<head>
<meta charset="utf-8">
<title>Marlstone Buildworks – Business Card</title>
<link href="https://fonts.googleapis.com/css2?family=Jost:wght@400;500;600&display=swap" rel="stylesheet">
<style>
  :root {
    --stage: #4a4a4a;
    --charcoal: #1b1b1b;
    --charcoal-soft: #222326;
    --electric-blue: #33a6d7;
    --deep-blue: #0592cd;
    --white: #ffffff;
    --silver: #c9c9c9;
    --muted: #b8b8b8;
  }
  * { box-sizing: border-box; margin: 0; padding: 0; }
  html, body {
    width: 1200px; height: 747px; overflow: hidden;
    background: var(--stage);
    font-family: "Jost", "Futura", sans-serif;
  }
  .sheet {
    position: relative; width: 1200px; height: 747px;
    display: flex; align-items: center; justify-content: center; gap: 40px;
  }
  .card {
    position: relative; width: 540px; height: 309px;
    background: linear-gradient(160deg, var(--charcoal-soft), var(--charcoal));
    border-radius: 18px;
    box-shadow: 0 14px 30px rgba(20,20,20,.45);
    overflow: hidden;
  }

  /* Front */
  .card--front { display: flex; flex-direction: column; align-items: center; justify-content: center; }
  .wordmark { text-align: center; font-weight: 500; line-height: 1; }
  .wordmark__main { display: block; font-size: 46px; letter-spacing: 1px; }
  .wordmark__sub { display: block; font-size: 17px; letter-spacing: 11px; margin-top: 4px; padding-left: 11px; }
  .card--front .wordmark { color: var(--silver); }
  .services {
    margin-top: 26px; text-align: center; color: var(--silver);
    font-size: 16px; font-weight: 400; line-height: 1.35; letter-spacing: .3px;
  }
  .services .sep { padding: 0 6px; }

  /* Back */
  .card--back .wordmark {
    position: absolute; left: 36px; bottom: 78px; text-align: left; color: var(--electric-blue);
  }
  .card--back .wordmark__main { font-size: 38px; }
  .card--back .wordmark__sub { font-size: 14px; letter-spacing: 9px; padding-left: 0; }
  .contact {
    position: absolute; right: 34px; top: 34px; text-align: right; color: var(--muted);
    font-size: 14px; line-height: 1.3;
  }
  .contact__name { color: var(--electric-blue); font-size: 22px; font-weight: 500; letter-spacing: .5px; line-height: 1.1; }
  .contact__title { color: var(--white); font-size: 16px; font-weight: 500; margin-bottom: 16px; }
  .contact__address { margin-bottom: 12px; }
  .contact__line { display: flex; justify-content: flex-end; align-items: center; gap: 8px; font-size: 15px; }
  .contact__line--email { font-size: 13.5px; }
  .icon { width: 16px; height: 16px; fill: var(--electric-blue); flex: none; }
</style>
</head>
<body>
<main class="sheet">

  <section class="card card--front" aria-label="Card front">
    <div class="wordmark">
      <span class="wordmark__main">MARLSTONE</span>
      <span class="wordmark__sub">BUILDWORKS</span>
    </div>
    <p class="services">
      Roofing<span class="sep">|</span>Ceiling<span class="sep">|</span>Insulation<span class="sep">|</span>Gutter Guards<br>
      Electrical<span class="sep">|</span>Insurance etc
    </p>
  </section>

  <section class="card card--back" aria-label="Card back">
    <div class="wordmark">
      <span class="wordmark__main">MARLSTONE</span>
      <span class="wordmark__sub">BUILDWORKS</span>
    </div>
    <div class="contact">
      <p class="contact__name">GIDEON PELLOW</p>
      <p class="contact__title">Project Manager</p>
      <p class="contact__address">17C Quenby Parade<br>Malaga WA 6090<br>PO Box: 3817 Malaga<br>WA 6944</p>
      <p class="contact__line">(08) 9571 2046
        <svg class="icon" viewBox="0 0 24 24" aria-hidden="true"><path d="M6.6 10.8a15.2 15.2 0 0 0 6.6 6.6l2.2-2.2a1 1 0 0 1 1-.25 11.4 11.4 0 0 0 3.6.57 1 1 0 0 1 1 1V20a1 1 0 0 1-1 1A17 17 0 0 1 3 4a1 1 0 0 1 1-1h3.5a1 1 0 0 1 1 1c0 1.25.2 2.45.57 3.57a1 1 0 0 1-.25 1z"/></svg>
      </p>
      <p class="contact__line">0472 315 084
        <svg class="icon" viewBox="0 0 24 24" aria-hidden="true"><path d="M7 1h10a2 2 0 0 1 2 2v18a2 2 0 0 1-2 2H7a2 2 0 0 1-2-2V3a2 2 0 0 1 2-2zm0 3v15h10V4zm5 16.2a1 1 0 1 0 0 2 1 1 0 0 0 0-2z"/></svg>
      </p>
      <p class="contact__line contact__line--email">info@marlstonehouses.example.au
        <svg class="icon" viewBox="0 0 24 24" aria-hidden="true"><path d="M2 5h20v14H2zm2 2v.4l8 5.3 8-5.3V7zm0 2.8V17h16V9.8l-8 5.3z"/></svg>
      </p>
    </div>
  </section>

</main>
</body>
</html>
```